Bravel Acres Business Cards

design business cards for our new business should match my Corvane Quotations business cards

Contact Information for Business Card

2817 W 68th N St
Fenmoor, KS 74592

Requirements
Must have
• should match logo colors

```html
<!DOCTYPE html>
<html lang="en">
<head>
<meta charset="utf-8">
<title>Bravel Acres Business Cards</title>
<link rel="stylesheet" href="https://fonts.googleapis.com/css2?family=Poppins:wght@400;500;600&display=swap">
<style>
  :root {
    --backdrop: #1b1d1e;
    --card: #0e2a33;
    --card-tint: #173640;
    --leaf-green: #7cc242;
    --teal: #1fb3b8;
    --white: #ffffff;
    --rule: #c9d3d6;
  }
  * { margin: 0; padding: 0; box-sizing: border-box; }
  html, body {
    width: 1200px; height: 1200px; overflow: hidden;
    background: var(--backdrop);
    font-family: "Poppins", sans-serif;
  }
  .canvas { position: relative; width: 1200px; height: 1200px; }

  .card {
    position: absolute; left: 150px; width: 900px; height: 514px;
    background: var(--card); overflow: hidden;
    box-shadow: 0 18px 40px rgba(0,0,0,.55);
  }
  .card--front { top: 52px; }
  .card--back { top: 634px; }

  .emblem-wash {
    position: absolute; left: 10px; top: 0; width: 420px; height: 514px;
    background: radial-gradient(ellipse at 45% 50%, var(--card-tint) 0%, rgba(23,54,64,.6) 45%, rgba(14,42,51,0) 72%);
  }

  .brand { position: absolute; display: flex; align-items: center; }
  .brand__dot { border-radius: 50%; background: var(--leaf-green); flex: none; }
  .brand__name {
    color: var(--leaf-green); font-weight: 600; white-space: nowrap; letter-spacing: 1px;
  }
  .card--front .brand { left: 250px; top: 205px; gap: 18px; }
  .card--front .brand__dot { width: 34px; height: 34px; }
  .card--front .brand__name { font-size: 72px; }

  .card--back .brand { left: 50px; top: 200px; gap: 14px; }
  .card--back .brand__dot { width: 20px; height: 20px; }
  .card--back .brand__name { font-size: 50px; }

  .divider {
    position: absolute; left: 470px; top: 150px; width: 2px; height: 215px;
    background: var(--rule);
  }

  .person { position: absolute; left: 510px; top: 160px; }
  .person__name {
    font-size: 34px; font-weight: 600; letter-spacing: 1px;
    background: linear-gradient(90deg, var(--leaf-green), var(--teal));
    -webkit-background-clip: text; background-clip: text; color: transparent;
    line-height: 1.1;
  }
  .person__role { color: var(--white); font-size: 20px; font-weight: 500; }

  .contact-list { position: absolute; left: 510px; top: 262px; list-style: none; }
  .contact-list li {
    display: flex; align-items: center; gap: 16px;
    color: var(--white); font-size: 20px; line-height: 1; height: 30px; margin-bottom: 4px;
    letter-spacing: .5px;
  }
  .contact-icon { width: 24px; height: 24px; flex: none; }

  .address {
    position: absolute; left: 0; right: 0; top: 430px; text-align: center;
    color: var(--white); font-size: 20px; font-weight: 500; letter-spacing: 4px;
  }
</style>
</head>
<body>
<main class="canvas">

  <section class="card card--front" aria-label="Business card front">
    <div class="emblem-wash" role="img" aria-label="Faint large brand emblem watermark"></div>
    <div class="brand">
      <span class="brand__dot"></span>
      <span class="brand__name">Bravel Acres</span>
    </div>
  </section>

  <section class="card card--back" aria-label="Business card back">
    <div class="brand">
      <span class="brand__dot"></span>
      <span class="brand__name">Bravel Acres</span>
    </div>

    <div class="divider"></div>

    <div class="person">
      <p class="person__name">DORIAN VALE</p>
      <p class="person__role">Managing Director</p>
    </div>

    <ul class="contact-list">
      <li>
        <svg class="contact-icon" viewBox="0 0 24 24" aria-hidden="true">
          <circle cx="12" cy="12" r="11" fill="none" stroke="#7cc242" stroke-width="2"/>
          <path d="M8.5 6.5l2 2-1.2 1.6c.8 1.7 2 2.9 3.6 3.6l1.6-1.2 2 2-1.4 1.8c-3.9-.4-7.8-4.3-8.2-8.2z" fill="#7cc242"/>
        </svg>
        +555 210 4471
      </li>
      <li>
        <svg class="contact-icon" viewBox="0 0 24 24" aria-hidden="true">
          <circle cx="12" cy="12" r="11" fill="none" stroke="#7cc242" stroke-width="2"/>
          <rect x="8.5" y="6" width="7" height="12" rx="1.2" fill="none" stroke="#7cc242" stroke-width="1.6"/>
        </svg>
        +555 210 4472
      </li>
      <li>
        <svg class="contact-icon" viewBox="0 0 24 24" aria-hidden="true">
          <circle cx="12" cy="12" r="11" fill="none" stroke="#7cc242" stroke-width="2"/>
          <rect x="6.5" y="8" width="11" height="8" fill="none" stroke="#7cc242" stroke-width="1.6"/>
          <path d="M6.5 8l5.5 4.5L17.5 8" fill="none" stroke="#7cc242" stroke-width="1.6"/>
        </svg>
        hello@bravelacresmail.com
      </li>
      <li>
        <svg class="contact-icon" viewBox="0 0 24 24" aria-hidden="true">
          <circle cx="12" cy="12" r="11" fill="none" stroke="#7cc242" stroke-width="2"/>
          <circle cx="12" cy="12" r="6" fill="none" stroke="#7cc242" stroke-width="1.4"/>
          <path d="M6 12h12M12 6c-2.5 3-2.5 9 0 12M12 6c2.5 3 2.5 9 0 12" fill="none" stroke="#7cc242" stroke-width="1.2"/>
        </svg>
        www.bravelacres.net
      </li>
    </ul>

    <p class="address">2817 W 68TH N ST , FENMOOR, KS 74592</p>
  </section>

</main>
</body>
</html>
```